Coach needs thank you cards (business card format) to deliver to customers. Model behavior

I am a coach who needs thank-you cards for customers and people to appreciate "exemplary behavior". First and foremost it is about the mindfulness of the people who have a great behavior to estimate and reward. The colors should contain silver and light like the logo of Mentorbrightpath.
Updates

The following should include the cards front and back. Front: Praise for: there should be room below to enter the name of the person. The fangs should be silver and light blue as on the logo which I have uploaded. Back: capitalized by date: exemplary behavior should be at the bottom right. mentorbrightpath.ch

```html
<!DOCTYPE html>
<html lang="de">
<head>
<meta charset="utf-8">
<title>Mentorbrightpath – Lobkarte</title>
<link rel="stylesheet" href="https://fonts.googleapis.com/css2?family=Questrial&family=Source+Sans+3:wght@500&display=swap">
<style>
  :root {
    --backdrop: #3a3a3a;
    --card-blue: #2173bb;
    --card-silver: #f0f0f0;
    --ink-blue: #2a6cb8;
    --paper-white: #ffffff;
  }
  html, body {
    margin: 0;
    padding: 0;
    width: 1200px;
    height: 900px;
    overflow: hidden;
    background: var(--backdrop);
  }
  .canvas {
    position: relative;
    width: 1200px;
    height: 900px;
  }
  .card {
    position: absolute;
    top: 269px;
    height: 357px;
    box-sizing: border-box;
  }
  .card--front {
    left: 52px;
    width: 538px;
    background: var(--card-blue);
  }
  .card--back {
    left: 613px;
    width: 544px;
    background: var(--card-silver);
  }
  .front-title {
    position: absolute;
    left: 0;
    right: 0;
    top: 150px;
    margin: 0;
    text-align: center;
    font-family: "Questrial", sans-serif;
    font-weight: 400;
    font-size: 24px;
    letter-spacing: 0.3px;
    color: var(--paper-white);
  }
  .name-field {
    position: absolute;
    left: 86px;
    top: 183px;
    width: 374px;
    height: 36px;
    background: var(--paper-white);
  }
  .back-title {
    position: absolute;
    left: 0;
    right: 0;
    top: 169px;
    margin: 0;
    text-align: center;
    font-family: "Questrial", sans-serif;
    font-weight: 400;
    font-size: 24px;
    letter-spacing: 0.2px;
    color: var(--ink-blue);
  }
  .web-address {
    position: absolute;
    left: 0;
    right: 0;
    top: 292px;
    text-align: center;
    font-family: "Source Sans 3", sans-serif;
    font-weight: 500;
    font-size: 17px;
    color: var(--ink-blue);
  }
</style>
</head>
<body>
  <main class="canvas">
    <section class="card card--front" aria-label="Vorderseite">
      <h1 class="front-title">EIN LOB FÜR</h1>
      <div class="name-field" aria-label="Feld für den Namen"></div>
    </section>
    <section class="card card--back" aria-label="Rückseite">
      <h2 class="back-title">VORBILDLICHES VERHALTEN</h2>
      <p class="web-address">www.mentorbrightpath.ch</p>
    </section>
  </main>
</body>
</html>
```